Radiant Crossing - An Exciting Mission & Book Cover Project

Help me to inspire people to live their best life! This is a mission, not just a design project.
I need a Book Cover designed to keep me inspired on the process of writing my book.
Book Title: Radiant Crossing
Tag Line: Three Simple Steps to get out of your own way, SuperCharge your Life and Step into Purpose!
Author: Marlis Quenby

The three steps are: Ownership, Vision and Action (Not sure if this should be on the front or back of the book cover)

The book is a self-help, motivational book. Personal development.
The cover needs to be strong and capture peoples attention, especially with competing shelf space. I almost see a fire ball of flame or explosion that will grab peoples attention.
My company is The Lantern Institute. I have added the company logo and a few pages of my presentation and topic outline to give an idea.
Maybe: The Lantern Institute logo on back of the cover. website is marlisquenby.com

THOUGHT: People should be able to take a photo of them holding the book cover showing what area of life they want Radiant Crossing in. This is why the front cover must be so visual and powerful that they want to take a photo with it. Ie. Explosion, fire, strong and bold.

Target Market(s)

Anyone who feels stuck and needs to breakthrough and move forward in life.

Industry/Entity Type

Motivation

Font styles to use
Serif
Sans Serif

Colors
ec1f27
f37122
fbed22

Requirements
Must have
• The design must be STRONG, SIMPLE, STAND OUT ON BOOK SHELVES.
Must have an open file to swap the photo and copy out.

Back Cover Page
1) Summary
2) 2-3 testimonials. One sentence.
3) About the Author (maybe with photo)
4) Lantern Institute logo
5) Website: radiantcrossing.com and marlisquenby.com
Nice to have
• If my photo works somewhere that would be great. I will change the photo later.
Added Where's Your Harbor? a nice cover example.
Should not have
• Right now I am writing the summary for the back of the cover. For now use Loreum Ipsum text and 2-3 recommendations. Again, I will get these only later.

```html
<!DOCTYPE html>
<html lang="en">
<head>
<meta charset="utf-8">
<title>Radiant Crossing — Book Cover</title>
<link rel="stylesheet" href="https://fonts.googleapis.com/css2?family=Oswald:wght@700&family=Jost:ital,wght@0,400;0,700;1,600;1,700&family=Barlow+Condensed:wght@600&display=swap">
<style>
  :root {
    --page: #ffffff;
    --cover-white: #ffffff;
    --mist: #e6e6e6;
    --ink: #0d0d0d;
    --flame-red: #ec1f27;
    --flame-orange: #f37122;
    --spark-yellow: #f8ec23;
    --skin: #b07a55;
  }
  * { box-sizing: border-box; margin: 0; padding: 0; }
  html, body {
    width: 949px; height: 1200px; overflow: hidden; background: var(--page);
  }
  .cover {
    position: relative; width: 949px; height: 1200px;
    background: var(--cover-white);
  }
  .cover__art {
    position: absolute; left: 20px; right: 20px; top: 20px; height: 912px;
    background: linear-gradient(180deg, #ffffff 0%, #ffffff 55%, #f2f2f2 80%, var(--mist) 100%);
  }
  .hero-photo {
    position: absolute; left: 0; right: 0; top: 0; height: 640px;
    background:
      radial-gradient(ellipse 24% 36% at 52% 50%, var(--skin) 0%, #c98a4a 55%, var(--flame-orange) 78%, rgba(243,113,34,0) 100%),
      radial-gradient(ellipse 55% 70% at 50% 45%, #f4f4f4 0%, #ececec 60%, rgba(255,255,255,0) 100%),
      linear-gradient(180deg, #f6f6f6 0%, #ffffff 100%);
  }
  .title {
    position: absolute; left: 20px; right: 20px; text-align: center; line-height: 1;
  }
  .title__main {
    top: 598px; font-family: "Oswald", sans-serif; font-weight: 700;
    font-size: 150px; color: var(--flame-red); letter-spacing: 1px;
  }
  .title__second {
    top: 742px; font-family: "Jost", sans-serif; font-weight: 700;
    font-size: 98px; color: var(--ink); letter-spacing: -1px;
  }
  .subtitle {
    top: 836px; font-family: "Jost", sans-serif; font-style: italic; font-weight: 700;
    font-size: 46px; color: var(--flame-red);
  }
  .torn-edge {
    position: absolute; left: 20px; top: 904px; width: 909px; height: 30px;
  }
  .panel {
    position: absolute; left: 20px; right: 20px; top: 926px; height: 246px;
    background: var(--spark-yellow);
  }
  .tagline {
    position: absolute; left: 50px; right: 50px; top: 44px;
    text-align: center; font-family: "Barlow Condensed", sans-serif; font-weight: 600;
    font-size: 39px; line-height: 50px; color: var(--ink);
  }
  .bracket {
    position: absolute; width: 22px; height: 22px; border-color: var(--ink); border-style: solid;
  }
  .bracket--open { left: 42px; top: 38px; border-width: 2px 0 0 2px; }
  .bracket--close { right: 42px; top: 132px; border-width: 0 2px 2px 0; }
  .author {
    position: absolute; left: 0; right: 0; top: 166px; text-align: center;
    font-family: "Jost", sans-serif; font-size: 60px; line-height: 1; color: var(--ink);
  }
  .author__first { font-weight: 700; }
  .author__last { font-weight: 400; }
</style>
</head>
<body>
  <main class="cover">
    <div class="cover__art">
      <div class="hero-photo" role="img" aria-label="Photo of a businessman in a white shirt and loose tie tearing his shirt open to reveal a muscular torso surrounded by flames"></div>
    </div>

    <h1 class="title title__main">RADIANT</h1>
    <p class="title title__second">CROSSING</p>
    <p class="title subtitle">Rapid Life Transformation</p>

    <svg class="torn-edge" viewBox="0 0 909 30" preserveAspectRatio="none" aria-hidden="true">
      <path d="M0 22 L20 18 L38 24 L60 16 L82 22 L100 19 L124 25 L150 17 L172 23 L196 18 L220 24 L246 16 L270 22 L292 19 L318 25 L340 17 L364 23 L390 18 L414 24 L440 15 L462 22 L488 18 L512 24 L536 17 L560 23 L586 18 L610 25 L634 16 L660 22 L684 18 L708 24 L734 16 L758 23 L782 18 L806 24 L830 17 L856 23 L880 17 L909 22 L909 30 L0 30 Z" fill="#f8ec23"/>
      <path d="M0 22 L20 18 L38 24 L60 16 L82 22 L100 19 L124 25 L150 17 L172 23 L196 18 L220 24 L246 16 L270 22 L292 19 L318 25 L340 17 L364 23 L390 18 L414 24 L440 15 L462 22 L488 18 L512 24 L536 17 L560 23 L586 18 L610 25 L634 16 L660 22 L684 18 L708 24 L734 16 L758 23 L782 18 L806 24 L830 17 L856 23 L880 17 L909 22" fill="none" stroke="#ffffff" stroke-width="4"/>
    </svg>

    <section class="panel">
      <span class="bracket bracket--open"></span>
      <p class="tagline">Three Simple Steps to get out of your own way,<br>SuperCharge your Life and Step into Purpose!</p>
      <span class="bracket bracket--close"></span>
      <p class="author"><span class="author__first">MARLIS</span> <span class="author__last">QUENBY</span></p>
    </section>
  </main>
</body>
</html>
```